Agriculture Business Need a Responsive Web Design

We need a Responsive Web Design for a Agriculture Business
We deliver agriculture data insight for farmers, media, salespersons and other that have an interrest in Agriculture.
Our products is a Velorind - a application that helps people with insight on farms, and what this farms have deliveried of products. Products like Milk, grains, eggs, slaughtering of livestock, chicken, sheep and other slaughter of animals. Data about size of farms. We deliver stats about these farms. Compeare farms.

Agriculture businesses

Agriculture

1 page

Sans Serif

• Responsive design. I.e the design shall be used on smartphones to desktop browsers. I think 2 columns on big screens that will collapse to 1 one small screens.

```html
<!DOCTYPE html>
<html lang="en">
<head>
<meta charset="utf-8">
<title>Velorind — Pricing</title>
<link href="https://fonts.googleapis.com/css2?family=Raleway:wght@500;600;700;800&family=Open+Sans:wght@400;600;700&display=swap" rel="stylesheet">
<style>
:root{
  --ink:#2f2f2f;
  --muted:#6b6b6b;
  --line:#e2e2e2;
  --green:#7cbd2a;
  --green-dark:#6aa821;
  --blue:#6fc0d5;
  --blue-dark:#5faabe;
  --gold:#dcaa4c;
  --gold-dark:#c89a43;
  --band:#6cc0d6;
  --footer:#2a2a2a;
  --footer-text:#c9c9c9;
  --white:#fff;
}
*{box-sizing:border-box;margin:0;padding:0}
html,body{width:687px;height:1200px;overflow:hidden;background:var(--white)}
body{position:relative;font-family:"Open Sans",Arial,sans-serif;color:var(--ink)}
.abs{position:absolute}
.heading{font-family:"Raleway",Arial,sans-serif}

/* header */
.site-header{position:absolute;left:0;top:0;width:687px;height:50px;border-top:2px solid var(--green);background:var(--white)}
.brand{position:absolute;left:56px;top:10px;display:flex;align-items:center;gap:7px}
.brand-dot{width:28px;height:28px;border-radius:50%;background:var(--gold)}
.brand-name{font-family:"Raleway",sans-serif;font-weight:700;font-size:14px;letter-spacing:.5px;color:#3a3a3a}
.main-nav{position:absolute;left:224px;top:20px;display:flex;gap:14px;font-family:"Raleway",sans-serif;font-weight:600;font-size:7.2px;color:#333}
.main-nav .active{color:var(--green)}
.nav-icon{position:absolute;top:12px;width:27px;height:27px;border-radius:50%;border:2px solid}
.nav-icon.lock{left:571px;border-color:var(--gold)}
.nav-icon.edit{left:602px;border-color:var(--green)}

/* hero */
.hero{position:absolute;left:0;top:50px;width:687px;height:199px;background:linear-gradient(180deg,#5d7440 0%,#7e8f4c 45%,#a9a679 70%,#8a8a4e 100%)}
.hero-title{position:absolute;left:0;width:100%;top:82px;text-align:center;font-family:"Raleway",sans-serif;font-weight:800;font-size:32px;color:var(--white);letter-spacing:.5px}
.dots{position:absolute;display:flex;gap:3px}
.dot{width:9px;height:9px;border-radius:50%;border:1.5px solid var(--white)}
.dot.on{background:var(--green)}

/* pricing */
.section-title{position:absolute;left:0;width:100%;text-align:center;font-family:"Raleway",sans-serif;font-weight:600;color:#222}
.pricing-sub{position:absolute;top:300px;width:100%;text-align:center;font-size:9.6px;color:var(--blue)}
.pricing-sub a{color:var(--green);text-decoration:underline}
.plan{position:absolute;top:336px;width:178px;height:223px;border:1px solid var(--line);text-align:center}
.plan-name{height:25px;line-height:25px;color:var(--white);font-family:"Raleway",sans-serif;font-weight:600;font-size:11px}
.plan-price{height:40px;color:var(--white);display:flex;align-items:center;justify-content:center;gap:4px;font-family:"Raleway",sans-serif}
.plan-price b{font-size:19px;font-weight:800}
.plan-price sup{font-size:9px;font-weight:800}
.plan-price span{font-family:"Open Sans",sans-serif;font-size:7.2px;margin-top:8px}
.plan ul{list-style:none;padding-top:11px;font-size:6.5px;color:#666}
.plan li{height:20px}
.plan li b{color:#333}
.plan-btn{display:inline-block;margin-top:6px;padding:0 10px;height:22px;line-height:22px;color:var(--white);font-family:"Raleway",sans-serif;font-weight:700;font-size:7.4px;border-radius:2px}
.starter{left:56px}.starter .plan-name,.starter .plan-btn{background:var(--green)}.starter .plan-price{background:var(--green-dark)}
.standard{left:254px}.standard .plan-name,.standard .plan-btn{background:var(--blue)}.standard .plan-price{background:var(--blue-dark)}
.premium{left:453px}.premium .plan-name,.premium .plan-btn{background:var(--gold)}.premium .plan-price{background:var(--gold-dark)}

/* testimonials */
.reviews{position:absolute;left:0;top:595px;width:687px;height:169px;background:linear-gradient(100deg,#5a3e2e 0%,#6e6460 45%,#8d9197 70%,#5f6570 100%)}
.review{position:absolute;top:30px;width:178px;height:92px;border:1.5px solid rgba(255,255,255,.85);border-radius:3px;color:var(--white);padding:7px 8px;font-size:6.6px;background:rgba(255,255,255,.06)}
.avatar{position:absolute;left:8px;top:7px;width:26px;height:26px;background:#b9a08a}
.review-name{position:absolute;left:42px;top:6px;font-weight:600;font-size:8.4px}
.review-handle{position:absolute;left:42px;top:18px;color:#e6e6e6}
.follow{position:absolute;right:8px;top:7px;border:1px solid rgba(255,255,255,.85);border-radius:2px;padding:1px 5px;font-size:6px}
.review-text{position:absolute;left:8px;top:38px;right:8px;line-height:1.55}
.review-text em{font-style:normal;color:#4fc3e0}
.review-meta{position:absolute;left:8px;top:64px;font-size:6px}
.review-stats{position:absolute;left:8px;top:77px;font-size:6.2px;letter-spacing:.5px}
.arrow{position:absolute;top:65px}

/* partners */
.partner{position:absolute;top:827px;width:88px;height:42px;border:1px solid #ddd;display:flex;align-items:center;justify-content:center;font-family:"Open Sans",sans-serif;font-weight:600;font-size:10px;color:#3f5f7a}

/* demo band */
.demo{position:absolute;left:0;top:900px;width:687px;height:120px;background:var(--band);text-align:center;color:var(--white)}
.demo h2{margin-top:26px;font-family:"Raleway",sans-serif;font-weight:600;font-size:14px}
.demo p{margin-top:8px;font-size:7.6px;color:#e9f7fb}
.demo-btn{display:inline-block;margin-top:12px;width:102px;height:31px;line-height:31px;background:var(--green);font-family:"Raleway",sans-serif;font-weight:700;font-size:9px;border-radius:2px}

/* footer */
.site-footer{position:absolute;left:0;top:1020px;width:687px;height:180px;background:var(--footer);color:var(--footer-text)}
.footer-brand{position:absolute;left:56px;top:56px;display:flex;align-items:center;gap:7px}
.footer-brand .brand-name{color:var(--white)}
.footer-col{position:absolute;top:20px;font-size:6.5px;line-height:13.2px}
.footer-col h4{font-family:"Raleway",sans-serif;font-weight:600;font-size:8.6px;color:var(--white);margin-bottom:7px}
.footer-rule{position:absolute;left:56px;right:56px;top:140px;height:1px;background:#3a3a3a}
.copyright{position:absolute;left:56px;top:155px;font-size:6.5px}
.socials{position:absolute;left:549px;top:151px;display:flex;gap:4px}
.socials span{width:19px;height:19px;border-radius:50%;border:1.5px solid var(--white)}
</style>
</head>
<body>

<header class="site-header">
  <div class="brand"><span class="brand-dot"></span><span class="brand-name">VELORIND</span></div>
  <nav class="main-nav">
    <span>HOME</span><span>ABOUT US</span><span>PRODUCTS</span><span>FEATURES</span><span>BLOG</span><span class="active">PRICING</span><span>CONTACT US</span>
  </nav>
  <svg class="abs" style="left:557px;top:22px" width="8" height="8" viewBox="0 0 8 8"><circle cx="3.2" cy="3.2" r="2.4" fill="none" stroke="#333" stroke-width="1.2"/><line x1="5" y1="5" x2="7.5" y2="7.5" stroke="#333" stroke-width="1.3"/></svg>
  <span class="nav-icon lock"></span>
  <svg class="abs" style="left:580px;top:20px" width="10" height="11" viewBox="0 0 10 11"><path d="M2.5 5V3.5a2.5 2.5 0 0 1 5 0V5" fill="none" stroke="#dcaa4c" stroke-width="1.4"/><rect x="1" y="5" width="8" height="6" rx="1" fill="#dcaa4c"/></svg>
  <span class="nav-icon edit"></span>
  <svg class="abs" style="left:610px;top:20px" width="11" height="11" viewBox="0 0 11 11"><path d="M1 10l1-3 6-6 2 2-6 6z" fill="#7cbd2a"/></svg>
</header>

<section class="hero" role="img" aria-label="Shepherd walking with a flock of sheep across a green hillside pasture">
  <h1 class="hero-title">PRICING</h1>
  <div class="dots" style="left:320px;top:172px"><span class="dot on"></span><span class="dot"></span><span class="dot"></span><span class="dot"></span></div>
</section>

<section class="pricing">
  <h2 class="section-title" style="top:276px;font-size:13px">CLOUD HOSTING SOLUTIONS</h2>
  <p class="pricing-sub">For details, prices, and additional service packages <a>click here</a></p>

  <div class="plan starter">
    <div class="plan-name">STARTER</div>
    <div class="plan-price"><b>$44</b><sup>99</sup><span>Per month</span></div>
    <ul>
      <li>At vero eos et accusamus et : <b>$56</b></li>
      <li>Blanditiis praesent : <b>$60</b></li>
      <li>Dignissimos ducimus qui : <b>$600 Monthly</b></li>
      <li>Sit voluptatem accusa : <b>$4</b></li>
      <li>Aliquam quaerat : <b>Every 24 hours</b></li>
    </ul>
    <span class="plan-btn">SUBSCRIBE</span>
  </div>
  <div class="plan standard">
    <div class="plan-name">STANDARD</div>
    <div class="plan-price"><b>$89</b><sup>99</sup><span>Per month</span></div>
    <ul>
      <li>At vero eos et accusamus et : <b>$56</b></li>
      <li>Blanditiis praesent : <b>$60</b></li>
      <li>Dignissimos ducimus qui : <b>$600 Monthly</b></li>
      <li>Sit voluptatem accusa : <b>$4</b></li>
      <li>Aliquam quaerat : <b>Every 24 hours</b></li>
    </ul>
    <span class="plan-btn">SUBSCRIBE</span>
  </div>
  <div class="plan premium">
    <div class="plan-name">PREMIUM</div>
    <div class="plan-price"><b>$134</b><sup>99</sup><span>Per month</span></div>
    <ul>
      <li>At vero eos et accusamus et : <b>$56</b></li>
      <li>Blanditiis praesent : <b>$60</b></li>
      <li>Dignissimos ducimus qui : <b>$600 Monthly</b></li>
      <li>Sit voluptatem accusa : <b>$4</b></li>
      <li>Aliquam quaerat : <b>Every 24 hours</b></li>
    </ul>
    <span class="plan-btn">SUBSCRIBE</span>
  </div>
</section>

<section class="reviews" role="img" aria-label="Desk with laptop, coffee cup and printed charts behind customer reviews">
  <svg class="arrow" style="left:20px" width="10" height="18" viewBox="0 0 10 18"><path d="M9 1L1 9l8 8" fill="none" stroke="#fff" stroke-width="1.6"/></svg>
  <svg class="arrow" style="left:657px" width="10" height="18" viewBox="0 0 10 18"><path d="M1 1l8 8-8 8" fill="none" stroke="#fff" stroke-width="1.6"/></svg>

  <article class="review" style="left:56px">
    <div class="avatar" role="img" aria-label="Reviewer photo"></div>
    <div class="review-name">Tom Reed</div><div class="review-handle">@reed</div>
    <span class="follow">Follow</span>
    <p class="review-text">Neque porro <em>@fieldHub</em> est, qui dolorem ips quia dolor sit amet on</p>
    <div class="review-meta" style="top:64px">05:07 Pm - 12 Dec 2015</div>
    <div class="review-stats">↩(0) &nbsp;⇄(2) &nbsp;♥(4)</div>
  </article>
  <article class="review" style="left:254px">
    <div class="avatar" role="img" aria-label="Reviewer photo" style="background:#c8b49a"></div>
    <div class="review-name">Lena</div><div class="review-handle">@lena</div>
    <span class="follow">Follow</span>
    <p class="review-text">Neque porro <em>@fieldHub</em> est, qui dolorem ips quia dolor sit amet on</p>
    <div class="review-meta">05:07 Pm - 12 Dec 2015</div>
    <div class="review-stats">↩(0) &nbsp;⇄(2) &nbsp;♥(4)</div>
  </article>
  <article class="review" style="left:453px">
    <div class="avatar" role="img" aria-label="Reviewer photo" style="background:#d19a5f"></div>
    <div class="review-name">Ruth</div>
    <div class="review-handle" style="color:#f3c21c;letter-spacing:1px">★★★★★</div>
    <span class="follow">Review</span>
    <div class="abs" style="left:42px;top:28px;font-size:6.2px">(7) &nbsp; (2)</div>
    <p class="review-text" style="top:48px">Neque porro est, qui dolorem ips quia dolor sit amet dolorem ips quia dt on</p>
    <div class="review-meta" style="top:76px">05:07 Pm - 12 Dec 2015</div>
  </article>
  <div class="dots" style="left:334px;top:141px"><span class="dot on" style="width:8px;height:8px"></span><span class="dot" style="width:8px;height:8px"></span></div>
</section>

<section class="partners">
  <h2 class="section-title" style="top:792px;font-size:13px">OVER 300 MILLION FOLLOWERS SERVED DAILY</h2>
  <svg class="abs" style="left:56px;top:842px" width="7" height="12" viewBox="0 0 7 12"><path d="M6 1L1 6l5 5" fill="none" stroke="#999" stroke-width="1.3"/></svg>
  <svg class="abs" style="left:623px;top:842px" width="7" height="12" viewBox="0 0 7 12"><path d="M1 1l5 5-5 5" fill="none" stroke="#999" stroke-width="1.3"/></svg>
  <div class="partner" style="left:104px">Swiftline</div>
  <div class="partner" style="left:201px">Envoya</div>
  <div class="partner" style="left:298px">Corvana</div>
  <div class="partner" style="left:396px">Upward Lane</div>
  <div class="partner" style="left:493px">Skillyard</div>
</section>

<section class="demo">
  <h2>SCHEDULE A DEMO TO SEE OUR FULL APPLICATION IN ACTION</h2>
  <p>At vero eos et accusamus dignissimos ducimus qui blanditiis praesentium voluptatum corrupt</p>
  <span class="demo-btn">GET STARTED</span>
</section>

<footer class="site-footer">
  <div class="footer-brand"><span class="brand-dot"></span><span class="brand-name">VELORIND</span></div>
  <div class="footer-col" style="left:198px"><h4>About us</h4>Our Story<br>Team<br>Newsletters<br>Contact<br>Jobs<br>Help Us Grow</div>
  <div class="footer-col" style="left:270px"><h4>Products</h4>Fieldwork Projects<br>Fieldwork Desk<br>Fieldwork Chat</div>
  <div class="footer-col" style="left:362px"><h4>Links</h4>Desktop Timer App<br>Office Apps for Business<br>Tablet App<br>Phone App<br>Mobile App</div>
  <div class="footer-col" style="left:474px"><h4>Resources</h4>Roadmap &amp; Updates<br>Security<br>Privacy Policy<br>Terms of Service<br>Webinars<br>Free for Startups</div>
  <div class="footer-col" style="left:574px"><h4>Legal</h4>Certified Trainers<br>Fieldwork<br>Developer Zone<br>Referral Program<br>Refund Policy<br>Login</div>
  <div class="footer-rule"></div>
  <p class="copyright">Copyrights © 2016, Velorind. All rights reserved.</p>
  <div class="socials"><span></span><span></span><span></span><span></span></div>
</footer>

</body>
</html>
```